Sports Nutrition Supplement Label design

We need a sports supplement label design for an existing business. (I have provided our business logo in the file uploads) These labels will remain consistent across the product line with the name of the product being the only changing field. The current product names (example: "vegan") on the labels provided are just for reference, the ingredients portions etc are final, but the actual name will be changed to something less generic for each product. I will just need to be able to change the name and have it match with label concept. We would like the look to be professional, clean, and exemplify quality. Please reference our business website tidelinevigor.com to get a feel for design and brand association.
I have also included the NKB supplement label guidelines so we are certain to maintain compliance.
Thank you and I'm looking forward to working with you and seeing your creative designs!
Darin

Target Market(s)

Athletes, Sports professionals, Colleges, Professional Sports Teams

Industry/Entity Type

Sports Science/ Sports Training/Athletics

Requirements
Nice to have
• I would like the design to possibly reflect these key terms: Sport Science, Chemistry, Clean, Professional, Quality (We also like water/ocean/waves concepts but is not a "requirement" it would have to really work well in the design somehow to appeal to wide range of athletes)

```html
<!DOCTYPE html>
<html lang="en">
<head>
<meta charset="utf-8">
<title>Tideline Vigor BCAA Label</title>
<link href="https://fonts.googleapis.com/css2?family=Anton&family=Montserrat:wght@500&family=Open+Sans:ital,wght@0,400;0,600;0,700;1,600&family=Oswald:wght@300;400;600&display=swap" rel="stylesheet">
<style>
  :root{
    --teal:#0b6661;
    --lime:#b1d234;
    --red:#e8212b;
    --silver:#cfd0d4;
    --ink:#111;
    --paper:#fff;
    --bg:#dedfe1;
    --rule:#e3e4e6;
  }
  html,body{margin:0;padding:0;width:1200px;height:1200px;overflow:hidden;background:var(--bg);}
  .canvas{position:relative;width:1200px;height:1200px;}
  .label{
    position:absolute;left:30px;top:385px;width:1424px;height:538px;
    transform:scale(0.8);transform-origin:0 0;
    background:var(--paper);overflow:hidden;
    font-family:"Open Sans",sans-serif;color:var(--ink);
  }
  .label-bands{position:absolute;inset:0;}
  .abs{position:absolute;}
  .intro{left:30px;top:12px;width:300px;margin:0;font-size:12.4px;line-height:17.8px;}
  .benefits{left:30px;top:172px;margin:0;padding:0;list-style:none;color:var(--paper);font-size:12.6px;line-height:17.8px;}
  .benefits li::before{content:"• ";font-size:9px;}
  .note-box{background:var(--paper);border:1.5px solid var(--ink);padding:3px 7px;font-size:10.4px;line-height:12.8px;box-sizing:border-box;width:292px;left:30px;}
  .note-box b{font-weight:700;}
  .directions{top:307px;height:59px;}
  .warning{top:377px;height:48px;}
  .disclaimer{top:435px;height:47px;}
  .lot{left:30px;top:489px;font-size:12px;line-height:17px;}
  .lot b{font-weight:700;}

  .brand{left:545px;top:40px;width:335px;text-align:center;}
  .brand-name{font-family:"Montserrat",sans-serif;font-weight:500;font-size:44px;letter-spacing:5px;line-height:1;margin-left:5px;}
  .brand-sub{font-family:"Montserrat",sans-serif;font-weight:500;font-size:13px;letter-spacing:9px;margin-top:14px;margin-left:9px;}

  .product-name{left:592px;top:172px;font-family:"Anton",sans-serif;font-size:122px;line-height:1;color:var(--silver);letter-spacing:1px;}
  .product-sub{left:594px;top:287px;font-family:"Oswald",sans-serif;font-weight:300;font-size:24px;line-height:30px;color:var(--paper);white-space:nowrap;}

  .ph{background:linear-gradient(135deg,#c3e04c,var(--lime));border-radius:6px;}
  .athletes{left:592px;top:341px;width:84px;height:68px;}

  .claims{left:730px;top:336px;}
  .claim{position:absolute;width:190px;height:26px;background:var(--red);color:var(--paper);
    font-family:"Oswald",sans-serif;font-weight:300;font-style:italic;font-size:15px;line-height:26px;padding-left:12px;
    transform:skewX(-10deg) rotate(-7deg);transform-origin:left center;white-space:nowrap;}
  .claim span{display:inline-block;transform:skewX(-4deg);}

  .flavor-fruit{left:505px;top:447px;width:60px;height:56px;border-radius:50%;background:radial-gradient(circle at 40% 40%,#fff27a,#f1d21c);}
  .flavor{left:572px;top:438px;}
  .flavor-name{font-family:"Anton",sans-serif;font-size:37px;line-height:1.05;color:var(--teal);}
  .flavor-sub{font-size:14px;}
  .netwt{left:804px;top:447px;font-family:"Oswald",sans-serif;}
  .netwt-line{font-weight:300;font-size:15px;}
  .netwt-type{font-weight:600;font-size:17px;margin-top:2px;}

  .facts{left:1098px;top:41px;width:283px;height:250px;border:2.5px solid var(--ink);box-sizing:border-box;padding:4px 7px;background:var(--paper);}
  .facts-title{font-weight:700;font-size:27px;line-height:32px;text-align:center;}
  .facts-meta{font-size:11px;line-height:13px;}
  .facts-meta b{font-weight:700;}
  .facts table{width:100%;border-collapse:collapse;margin-top:4px;border-top:3px solid var(--ink);}
  .facts th{font-size:9.5px;font-weight:700;text-align:right;padding:1px 0;border-bottom:1px solid var(--ink);}
  .facts td{font-size:12.4px;height:19.2px;border-bottom:1px solid var(--ink);padding:0;}
  .facts td small{font-family:"Oswald",sans-serif;font-weight:300;font-size:10.5px;}
  .facts td.amt{text-align:right;padding-right:8px;}
  .facts td.dv{text-align:right;width:36px;}
  .facts tr:last-child td{border-bottom:3px solid var(--ink);}
  .facts-foot{font-size:10.5px;margin-top:2px;}
  .other{left:1097px;top:297px;width:300px;color:var(--paper);font-size:11.6px;line-height:16px;}
  .other b{font-weight:700;}
  .badges{left:1098px;top:366px;display:flex;gap:15px;}
  .badge{width:44px;height:44px;border-radius:50%;background:#2d6db5;border:2px solid #fff;box-sizing:border-box;}
  .badge.green{background:#6aa843;}
  .badge.grey{background:#9a9ca0;}
  .badge.flat{background:#3f9a3f;border-radius:6px;border:none;}
  .distributor{left:1097px;top:442px;font-weight:700;font-size:20px;line-height:24.5px;}
</style>
</head>
<body>
<div class="canvas">
  <section class="label">
    <svg class="label-bands" width="1424" height="538" viewBox="0 0 1424 538" aria-hidden="true">
      <rect x="0" y="137" width="870" height="8" fill="var(--rule)"/>
      <polygon points="940,40 955,40 856,145 841,145" fill="var(--rule)"/>
      <polygon points="986,0 1424,0 1424,145 862,145" fill="var(--lime)"/>
      <rect x="0" y="154" width="1424" height="263" fill="var(--teal)"/>
      <rect x="0" y="427" width="1424" height="111" fill="var(--lime)"/>
      <polygon points="800,427 1424,427 1424,538 700,538" fill="var(--paper)"/>
      <polygon points="800,427 814,427 714,538 700,538" fill="var(--rule)"/>
      <rect x="810" y="427" width="614" height="6" fill="var(--rule)"/>
    </svg>

    <p class="abs intro">Our BCAA Powder is a blend of 5g of Branched Chain Amino Acids and Glutamine for lean muscle and recovery. Vitamin B6 is added to enhance the absorption of BCAAs. Branch Chain Amino Acids are the most abundant amino acids found in muscle tissue, and are the most readily absorbed group of amino acids. Our BCAA contains the ideal ratio of 2 parts Leucine to 1 part Isoleucine and Valine.</p>

    <ul class="abs benefits">
      <li>Vegan BCAAs</li>
      <li>BCAA Ratio 2:1:1</li>
      <li>Supports Muscle Building</li>
      <li>Speeds Recovery*</li>
      <li>Instantized to Dissolve Quickly</li>
      <li>Amazing Taste</li>
      <li>50 Servings Per Bottle</li>
    </ul>

    <div class="abs note-box directions"><b>Directions:</b> Mix 6.5G (1 Scoop) in 6 - 8 ounces of cold beverage. It will take a few minutes for all the powder to dissolve in the beverage. Best taken pre/post-workout or between meals.</div>
    <div class="abs note-box warning"><b>Warnining:</b> If you have any health conditions, are pregnant, breastfeeding, or taking medication, ask a physician prior to Keep out of reach of small children.</div>
    <div class="abs note-box disclaimer">* These statements have not been evaluated by the NKB. This product is not intended to diagnose, treat, cure or prevent any disease.</div>
    <div class="abs lot">Lot # and Expiration Date Printed on Bottom of Bottle.<br><b>SKU:ROC110M</b></div>

    <div class="abs brand">
      <div class="brand-name">TIDELINE</div>
      <div class="brand-sub">VIGOR SPORTS</div>
    </div>

    <div class="abs product-name">BCAA</div>
    <div class="abs product-sub">Branched Chain Amino Acids</div>

    <div class="abs ph athletes" role="img" aria-label="Icon of two flexing athletes with a barbell"></div>

    <div class="abs claims">
      <div class="claim" style="left:8px;top:0"><span>BCAA Ratio 2:1:1</span></div>
      <div class="claim" style="left:3px;top:30px"><span>Supports Muscle Building</span></div>
      <div class="claim" style="left:-2px;top:60px"><span>Speeds Recovery*</span></div>
    </div>

    <div class="abs flavor-fruit" role="img" aria-label="Illustration of a lemon and lime slice"></div>
    <div class="abs flavor">
      <div class="flavor-name">Lemon Lime</div>
      <div class="flavor-sub">Natural &amp; Artificial Flavor</div>
    </div>

    <div class="abs netwt">
      <div class="netwt-line">NET WT. 325 G (11.46 OZ)</div>
      <div class="netwt-type">DIETARY SUPPLEMENT</div>
    </div>

    <div class="abs facts">
      <div class="facts-title">Supplement Facts</div>
      <div class="facts-meta"><b>Serving Size:</b> One Scoop (6.5 g)<br><b>Servings Per Container:</b> 50</div>
      <table>
        <tr><th colspan="2">Amount Per Serving</th><th>%DV</th></tr>
        <tr><td>Vitamin B6 <small>(as Pyridoxine HCl)</small></td><td class="amt">2mg</td><td class="dv">118%</td></tr>
        <tr><td>Sodium <small>(as Sodium Chloride)</small></td><td class="amt">20mg</td><td class="dv">&lt;1%</td></tr>
        <tr><td>Potassium <small>(as Potassium Citrate)</small></td><td class="amt">34mg</td><td class="dv">&lt;1%</td></tr>
        <tr><td>L-Leucine</td><td class="amt">2000mg</td><td class="dv">**</td></tr>
        <tr><td>L-Isoleucine</td><td class="amt">1000mg</td><td class="dv">**</td></tr>
        <tr><td>L-Valine</td><td class="amt">1000mg</td><td class="dv">**</td></tr>
        <tr><td>L-Glutamine</td><td class="amt">1000mg</td><td class="dv">**</td></tr>
      </table>
      <div class="facts-foot">** Daily Value (DV) not established</div>
    </div>

    <div class="abs other"><b>Other Ingredients:</b> Malic Acid, Natural &amp; Artificial Flavors, Citric Acid, Sucralose.</div>

    <div class="abs badges">
      <div class="badge"></div>
      <div class="badge green"></div>
      <div class="badge"></div>
      <div class="badge grey"></div>
      <div class="badge flat"></div>
    </div>

    <div class="abs distributor">Distributed By: Company Name<br>Street Address City, ST Zipcode<br>website or phone number</div>
  </section>
</div>
</body>
</html>
```